Property Auctions with Teodor Bramwick

Podcast cover art 3000px by 3000px. Eye catching for a weekly podcast. The words should read Property Auctions (large font) with Teodor Bramwick (smaller font)

I would like the font and colours to be similar to my book, a copy of which I have attached.

Target Market(s)

New and experienced property investors looking to purchase at a property auction

```html
<!DOCTYPE html>
<html lang="en">
<head>
<meta charset="utf-8">
<title>Property Auctions with Teodor Bramwick – Podcast Cover</title>
<link rel="stylesheet" href="https://fonts.googleapis.com/css2?family=Oswald:wght@500;700&family=Allura&display=swap">
<style>
  :root {
    --page-bg: #ffffff;
    --cover-top: #2f3a3d;
    --cover-bottom: #3d4a4c;
    --gold-light: #ffe27a;
    --gold-mid: #f5b82a;
    --gold-deep: #d98f12;
    --frame-gold: #b99a4e;
    --text-white: #ffffff;
    --placeholder-dark: #2a2f30;
  }
  * { margin: 0; padding: 0; box-sizing: border-box; }
  html, body {
    width: 1200px;
    height: 807px;
    overflow: hidden;
    background: var(--page-bg);
  }
  .cover {
    position: absolute;
    left: 230px;
    top: 33px;
    width: 740px;
    height: 740px;
    background: linear-gradient(180deg, var(--cover-top) 0%, var(--cover-bottom) 100%);
    text-align: center;
  }
  .cover-frame {
    position: absolute;
    inset: 25px;
    border: 1px solid var(--frame-gold);
  }
  .show-title {
    position: absolute;
    left: 0;
    right: 0;
    top: 40px;
    font-family: "Oswald", sans-serif;
    font-weight: 700;
    font-size: 114px;
    line-height: 104px;
    letter-spacing: 0;
    background: linear-gradient(180deg, var(--gold-light) 0%, var(--gold-mid) 55%, var(--gold-deep) 100%);
    -webkit-background-clip: text;
    background-clip: text;
    color: transparent;
  }
  .show-connector {
    position: absolute;
    left: 0;
    right: 0;
    top: 268px;
    font-family: "Allura", cursive;
    font-size: 58px;
    line-height: 56px;
    color: var(--text-white);
  }
  .host-name {
    position: absolute;
    left: 0;
    right: 0;
    top: 322px;
    font-family: "Oswald", sans-serif;
    font-weight: 500;
    font-size: 37px;
    line-height: 48px;
    letter-spacing: 0;
    color: var(--text-white);
  }
  .emblem-placeholder {
    position: absolute;
    left: 201px;
    top: 392px;
    width: 338px;
    height: 298px;
    background: linear-gradient(180deg, var(--gold-deep) 0%, var(--placeholder-dark) 55%, var(--placeholder-dark) 100%);
  }
</style>
</head>
<body>
  <main class="cover">
    <div class="cover-frame"></div>
    <h1 class="show-title">PROPERTY<br>AUCTIONS</h1>
    <p class="show-connector">With</p>
    <p class="host-name">TEODOR BRAMWICK</p>
    <div class="emblem-placeholder" role="img" aria-label="Podcast emblem area: gold-outlined house with a microphone"></div>
  </main>
</body>
</html>
```